Pelmora Tours - Astronomy in the Kimberley

Pelmora Tours requires a web page to advertise astronomy tours in the East Kimberley, Australia. It needs the following tabs - Home, Tours, Astronomy Events, Gallery, Testimonials, Contacts.

It should target tourists to the Kimberley.
We are unsure of which colours to go with at the moment but we have included our logo if it helps.

It should be mobile and tablet friendly.

Target Market(s)

Families, +40, Tourist, hobby astronomists,

Industry/Entity Type

Events

Number of Pages Required

3 page

Colors
3377b5
ffffff

Requirements
Must have
• Home, Tours, Astronomy Events, Gallery, Calendar, Testimonials, Contacts.
• 'Pelmora Tours' logo
Nice to have
• Pictures of portable amateur telescopes. Pictures of Lake Kununurra or Wyndham.
Should not have
• Pictures of extremely large professional telescopes.

```html
<!DOCTYPE html>
<html lang="en">
<head>
<meta charset="utf-8">
<title>Pelmora Tours</title>
<link rel="stylesheet" href="https://fonts.googleapis.com/css2?family=Ubuntu:wght@400;500;700&family=Open+Sans:wght@400;600;700&family=Noto+Serif:ital@1&display=swap">
<style>
:root{
  --blue:#1f7dc0;
  --blue-bright:#3a8fdc;
  --link:#2a78b8;
  --ink:#333;
  --muted:#8a8a8a;
  --dark:#2a2a2a;
  --footer:#242528;
  --panel:#f2f2f2;
  --gallery-bg:#ededed;
  --white:#fff;
}
*{box-sizing:border-box;margin:0;padding:0}
html,body{width:890px;height:1200px;overflow:hidden}
body{position:relative;background:var(--white);font-family:"Open Sans",sans-serif;color:var(--ink)}
.abs{position:absolute}
.topline{left:0;top:0;width:890px;height:2px;background:var(--dark)}
.brand{left:82px;top:30px;display:flex;align-items:center;gap:8px}
.brand-dot{width:26px;height:26px;border-radius:50%;background:var(--blue)}
.brand-name{font-family:"Ubuntu",sans-serif;font-size:24px;font-weight:500;color:var(--blue)}
.member{left:666px;top:2px;width:142px;height:30px;background:var(--dark);color:#fff;font-size:10px;display:flex;align-items:center;padding-left:13px;gap:7px}
.member .chev{width:11px;height:11px;border-radius:50%;background:var(--blue);display:flex;align-items:center;justify-content:center}
.member .flag{margin-left:10px;width:28px;height:14px;background:#3d6fb0;border:1px solid #5a8ad0}
.phone{left:566px;top:60px;display:flex;align-items:center;gap:8px;font-size:14.5px;color:#333}
.social{display:flex;gap:6px}
.social span{width:25px;height:25px;border-radius:50%;display:block}
.header-social{left:694px;top:58px}
.c-fb{background:#1d5fa3}.c-tw{background:#28a7e0}.c-rss{background:#ef8f15}.c-mail{background:#bdbdbd}.c-pin{background:#cc2127}
.nav{left:0;top:109px;width:890px;height:33px;background:var(--blue)}
.nav a{position:absolute;top:0;height:33px;line-height:33px;color:#fff;text-decoration:none;font-family:"Ubuntu",sans-serif;font-size:12.5px}
.nav .active{left:85px;top:-2px;height:35px;line-height:37px;width:58px;text-align:center;background:var(--dark);font-weight:700}
.hero{left:0;top:142px;width:890px;height:355px;background:radial-gradient(circle at 30% 95%,#e8a040 0%,#8a4a18 14%,#2a1c14 32%,transparent 50%),radial-gradient(circle at 72% 45%,#a86a28 0%,#5a3a1a 18%,transparent 40%),linear-gradient(180deg,#0f1a2c 0%,#151a22 45%,#1c1612 100%)}
.hero-title{left:85px;top:188px;font-family:"Ubuntu",sans-serif;font-size:29px;color:#fff}
.hero-title b{font-weight:700}
.hero-text{left:85px;top:231px;width:360px;font-size:13px;line-height:18px;color:#e8e8e8}
.slider-tab{left:413px;top:464px}
.hero-rule{left:0;top:497px;width:890px;height:5px;background:var(--blue)}
.booking{left:0;top:502px;width:890px;height:48px;background:var(--dark)}
.field{position:absolute;top:14px;height:24px;background:#fff;border-radius:3px;font-size:10px;color:#777;line-height:24px;padding-left:7px}
.field svg{position:absolute;right:0;top:0}
.reserve{position:absolute;left:709px;top:11px;width:95px;height:26px;background:var(--blue-bright);color:#fff;font-family:"Ubuntu",sans-serif;font-weight:700;font-size:14px;text-align:center;line-height:26px;border-radius:2px}
.section-title{font-family:"Open Sans",sans-serif;font-size:16px;font-weight:600;color:#333}
.event{position:absolute;width:196px;height:46px}
.event .thumb{position:absolute;left:0;top:0;width:44px;height:45px;border:2px solid #ddd;background:linear-gradient(180deg,#6d8fa8 0%,#8fae6a 45%,#4f8a2e 100%)}
.event h3{position:absolute;left:50px;top:0;font-weight:400;font-size:12.5px;color:var(--link)}
.event p{position:absolute;left:50px;top:20px;width:150px;font-size:9px;line-height:13.5px;color:#666}
.event p u{color:#333}
.view-all{left:85px;top:731px;font-size:10.5px;color:#444}
.arrows{left:776px;top:576px;font-size:16px;color:#444;letter-spacing:8px}
.quote{left:484px;top:606px;width:322px;height:104px;background:var(--panel);padding:16px 14px 0;font-family:"Noto Serif",serif;font-style:italic;font-size:12.8px;line-height:18.5px;color:#555;overflow:hidden;white-space:nowrap}
.quote-tail{left:498px;top:710px}
.author{left:522px;top:730px;font-size:10px;color:#444;font-weight:700}
.author i{color:var(--muted);font-weight:600}
.gallery{left:0;top:768px;width:890px;height:228px;background:var(--gallery-bg)}
.gallery-head{left:0;top:784px;width:890px;text-align:center;font-size:16px}
.gline{top:797px;height:1px;background:#d4d4d4}
.card{position:absolute;top:818px;width:174px;height:112px;background:#fff;padding:5px}
.card .img{width:100%;height:101px}
.caption{position:absolute;top:936px;width:180px}
.caption h4{font-weight:400;font-size:12.5px;color:#333}
.caption p{font-size:9px;line-height:12px;color:#999}
.footer{left:0;top:996px;width:890px;height:204px;background:var(--footer);color:#ddd}
.foot-h{font-size:12px;font-weight:700;color:#fff}
.sitemap{left:98px;top:1056px;list-style:none;font-size:9.5px;line-height:16.3px;color:#ccc}
.sitemap li::before{content:"•";margin-right:5px}
.contact{left:246px;top:1056px;font-size:9.5px;line-height:16.5px;color:#ccc}
.contact .row{position:relative;padding-left:17px;margin-bottom:9px}
.contact svg{position:absolute;left:0;top:3px}
.foot-social{left:474px;top:1062px}
.foot-social span{width:20px;height:20px}
.foot-brand{left:474px;top:1098px;display:flex;align-items:center;gap:8px;font-family:"Open Sans",sans-serif;font-weight:700;font-size:12px;color:#fff}
.foot-brand span{width:12px;height:12px;border-radius:50%;background:var(--blue-bright)}
.copy{left:475px;top:1126px;font-size:9.5px;line-height:14px;color:#ccc}
.foot-logo{left:672px;top:1078px;display:flex;align-items:center;gap:8px}
.foot-logo span{width:24px;height:24px;border-radius:50%;background:var(--blue-bright)}
.foot-logo b{font-family:"Ubuntu",sans-serif;font-weight:500;font-size:22px;color:#8c9096}
</style>
</head>
<body>
<div class="abs topline"></div>

<div class="abs brand"><span class="brand-dot"></span><span class="brand-name">Pelmora Tours</span></div>

<div class="abs member">
  <span class="chev"><svg width="5" height="7" viewBox="0 0 5 7"><path d="M4 0.5L1 3.5L4 6.5" stroke="#fff" stroke-width="1.3" fill="none"/></svg></span>
  Member Login<span class="flag"></span>
</div>

<div class="abs phone">
  <svg width="11" height="18" viewBox="0 0 11 18"><rect x="1" y="1" width="9" height="16" rx="1.5" stroke="#333" stroke-width="1.4" fill="none"/><line x1="4" y1="14" x2="7" y2="14" stroke="#333" stroke-width="1.4"/></svg>
  (800) 555-0142
</div>
<div class="abs social header-social" role="img" aria-label="Social links">
  <span class="c-fb"></span><span class="c-tw"></span><span class="c-rss"></span><span class="c-mail"></span>
</div>

<nav class="abs nav">
  <a class="active">Home</a>
  <a style="left:170px">Tours</a>
  <a style="left:234px">Astronomy Events</a>
  <a style="left:366px">Gallery</a>
  <a style="left:434px">Testimonials</a>
  <a style="left:535px">Contact Us</a>
</nav>

<div class="abs hero" role="img" aria-label="Night photo of travellers by a campfire beside a lit caravan"></div>
<div class="abs hero-title">Welcome to <b>Pelmora</b> Tours</div>
<p class="abs hero-text">Lorem ipsum dolor sit amet conc sectetur adipscing elit and has been ended in the industry and has been ended!.</p>
<svg class="abs slider-tab" width="96" height="34" viewBox="0 0 96 34">
  <path d="M8 2 Q9 0 12 0 H46 V34 H0 Z" fill="#1f7dc0"/>
  <path d="M50 0 H84 Q87 0 88 2 L96 34 H50 Z" fill="#1f7dc0"/>
  <path d="M27 10 L21 17 L27 24" stroke="#fff" stroke-width="3" fill="none"/>
  <path d="M69 10 L75 17 L69 24" stroke="#fff" stroke-width="3" fill="none"/>
</svg>
<div class="abs hero-rule"></div>

<div class="abs booking">
  <div class="field" style="left:82px;width:153px">Check In
    <svg width="26" height="24" viewBox="0 0 26 24"><line x1="0.5" y1="0" x2="0.5" y2="24" stroke="#ddd"/><rect x="8" y="6" width="11" height="11" stroke="#bbb" fill="none"/><line x1="8" y1="9" x2="19" y2="9" stroke="#bbb"/></svg></div>
  <div class="field" style="left:245px;width:153px">Choose Out
    <svg width="26" height="24" viewBox="0 0 26 24"><line x1="0.5" y1="0" x2="0.5" y2="24" stroke="#ddd"/><rect x="8" y="6" width="11" height="11" stroke="#bbb" fill="none"/><line x1="8" y1="9" x2="19" y2="9" stroke="#bbb"/></svg></div>
  <div class="field" style="left:408px;width:140px">Adults
    <svg width="12" height="24" viewBox="0 0 12 24"><rect x="0.5" y="2" width="11" height="20" fill="#f0f0f0" stroke="#ccc"/><path d="M3 11 L6 14 L9 11" stroke="#555" fill="none"/></svg></div>
  <div class="field" style="left:558px;width:140px">Children
    <svg width="12" height="24" viewBox="0 0 12 24"><rect x="0.5" y="2" width="11" height="20" fill="#f0f0f0" stroke="#ccc"/><path d="M3 11 L6 14 L9 11" stroke="#555" fill="none"/></svg></div>
  <div class="reserve">RESERVE</div>
</div>

<h2 class="abs section-title" style="left:82px;top:575px">Astronomy Events</h2>
<div class="event" style="left:82px;top:610px"><div class="thumb" role="img" aria-label="Event photo of a garden lawn"></div><h3>Lorem ipsum dolor</h3><p>Lorem ipsum dolor sit amet, cons tetur adipisicing el... <u>READ MORE</u></p></div>
<div class="event" style="left:279px;top:610px"><div class="thumb" role="img" aria-label="Event photo of a garden lawn"></div><h3>Lorem ipsum dolor</h3><p>Lorem ipsum dolor sit amet, cons tetur adipisicing el... <u>READ MORE</u></p></div>
<div class="event" style="left:82px;top:674px"><div class="thumb" role="img" aria-label="Event photo of a garden lawn"></div><h3>Lorem ipsum dolor</h3><p>Lorem ipsum dolor sit amet, cons tetur adipisicing el... <u>READ MORE</u></p></div>
<div class="event" style="left:279px;top:674px"><div class="thumb" role="img" aria-label="Event photo of a garden lawn"></div><h3>Lorem ipsum dolor</h3><p>Lorem ipsum dolor sit amet, cons tetur adipisicing el... <u>READ MORE</u></p></div>
<div class="abs view-all">View All News</div>

<h2 class="abs section-title" style="left:486px;top:575px">Client Testimonials</h2>
<div class="abs arrows">&lsaquo;&rsaquo;</div>
<blockquote class="abs quote">Sed mattis pretium ligula quis egestas. Proin adip<br>tempor. Fusce faucibus felis ut odio ullamcorper<br>tortor sodales. Ut luctus nibh nec dui blandit qui<br>facilisis.</blockquote>
<svg class="abs quote-tail" width="22" height="16" viewBox="0 0 22 16"><path d="M0 0 H22 V16 Z" fill="#f2f2f2"/></svg>
<div class="abs author">Marlon Vesk <i>- happy buyer</i></div>

<section class="abs gallery"></section>
<div class="abs gline" style="left:81px;width:250px"></div>
<div class="abs gline" style="left:556px;width:250px"></div>
<h2 class="abs section-title gallery-head"><span style="color:#bbb;margin-right:14px">&lsaquo;</span>Our Caravian Gallery<span style="color:#bbb;margin-left:14px">&rsaquo;</span></h2>

<div class="card" style="left:81px"><div class="img" role="img" aria-label="Star trails over a rock outcrop and camper at night" style="background:linear-gradient(180deg,#1c2438 0%,#2d3550 60%,#4a3a28 85%,#8a5a24 100%)"></div></div>
<div class="card" style="left:266px"><div class="img" role="img" aria-label="Four-wheel drive towing a caravan through a river crossing" style="background:linear-gradient(180deg,#4f6a3a 0%,#dcdcdc 45%,#8a9aa0 70%,#c8d0d2 100%)"></div></div>
<div class="card" style="left:447px"><div class="img" role="img" aria-label="Interior of a caravan with bed and kitchen" style="background:linear-gradient(180deg,#c9d2d8 0%,#a9b4bc 40%,#8a8a82 75%,#c9a24a 100%)"></div></div>
<div class="card" style="left:634px"><div class="img" role="img" aria-label="Four-wheel drive towing a caravan on a dusty track" style="background:linear-gradient(180deg,#6f7a5a 0%,#b8a48a 45%,#d6c6b2 70%,#8a6040 100%)"></div></div>

<div class="caption" style="left:84px"><h4>Lorem Ipsum dolor</h4><p>Lorem Ipsum est simplement du faux<br>texte employé dans.</p></div>
<div class="caption" style="left:270px"><h4>Lorem Ipsum dolor</h4><p>Lorem Ipsum est simplement du faux<br>texte employé dans.</p></div>
<div class="caption" style="left:452px"><h4>Lorem Ipsum dolor</h4><p>Lorem Ipsum est simplement du faux<br>texte employé dans.</p></div>
<div class="caption" style="left:640px"><h4>Lorem Ipsum dolor</h4><p>Lorem Ipsum est simplement du faux<br>texte employé dans.</p></div>

<footer class="abs footer"></footer>
<h3 class="abs foot-h" style="left:101px;top:1028px">Site Map</h3>
<h3 class="abs foot-h" style="left:246px;top:1028px">Contact us</h3>
<h3 class="abs foot-h" style="left:476px;top:1028px">Follow Us</h3>
<ul class="abs sitemap">
  <li>Home</li><li>Who We Are</li><li>Getting Started</li><li>Customer Experience</li><li>Professional</li><li>Testimonials</li>
</ul>
<div class="abs contact">
  <div class="row"><svg width="9" height="12" viewBox="0 0 9 12"><path d="M4.5 11.5 C1 7 0.5 5.5 0.5 4.5 A4 4 0 0 1 8.5 4.5 C8.5 5.5 8 7 4.5 11.5Z" fill="#bbb"/><circle cx="4.5" cy="4.5" r="1.6" fill="#242528"/></svg>Pelmora Tours Tamsin Orrell<br>48 Carrow Lane Dunmere,<br>WA 6743</div>
  <div class="row"><svg width="11" height="11" viewBox="0 0 11 11"><path d="M2 0.5 L4 3 L3 4.5 C4 6.5 5 7.5 6.5 8 L8 7 L10.5 9 L9 10.5 C4.5 10.5 0.5 6.5 0.5 2Z" fill="#bbb"/></svg>800.555.0199</div>
  <div class="row"><svg width="12" height="9" viewBox="0 0 12 9"><rect x="0.5" y="0.5" width="11" height="8" fill="none" stroke="#bbb"/><path d="M0.5 0.5 L6 5 L11.5 0.5" fill="none" stroke="#bbb"/></svg>hello@pelmoratours.example</div>
</div>
<div class="abs social foot-social" role="img" aria-label="Social links">
  <span class="c-fb" style="background:#3b6bb5"></span><span class="c-tw"></span><span class="c-rss"></span><span class="c-pin"></span>
</div>
<div class="abs foot-brand"><span></span>PELMORA</div>
<div class="abs copy">copyright©2015.Pelmoratours<br>All Rights Reserved</div>
<div class="abs foot-logo"><span></span><b>Pelmora</b></div>
</body>
</html>
```